Need A Modern Website Design For ADSL2+ Provider

AIM: To sell affordable combined ADSL2+ Unlimited & phone line rentals to residential customers.

TYPE: This project is for DESIGN only (no code)

Source Files: I need all source files, fonts, images to be provided in ZIP format.

Logo: Existing (attached)

-Corporate Colours-
Black & Red (Same as Logo)
Others colours are fine as long as it looks corporate and modern.

-Pages-
Need another page to display our pricing plan

(1)Homepage Design
(2)Page to display our plans (needs to be in tables)
Example: http://lnkshrt.example/Qv7Rp2

-Pricing Plan-
(1) $59.95 / Month (Metro / City Areas)
(2) $79.95 / Month (Outside City Areas / Rural Areas)
Detailed Pricing plans is in PDF attached
Updates

Just letting everyone know we have picked a designer, thank you for all you submissions.

Target Market(s)

Both male & female, Young & Old

Industry/Entity Type

Residential

Requirements
Must have
• + Graphic banner on the home page that shows our ADSL2+ combo plan for ADSL2+ Unlimited & Phone Line Rental for only $59.95

+ A box to allow customers to login to their account (username & password + login button)

+ Clearly display contact number
+ Button to sign up
+ Button to check service availability something like https://linkup.vexora.com/wizard/

+ Button for Live Chat
+ Navigation menu
+ Social media icons Chatterly, Plexo +, Chirpnet
+ Minimal text on homepage
+ Corporate & Friendly
Nice to have
• + Effective use of icons with corporate colours
+ Effective use of stockphotos
(use of people in photos would be nice)

+ Effective use of graphics to navigate people through the site and inform customers of specials,etc.
Should not have
• + Cluttered
+ Don’t want long scrolling homepage
+ Don’t want too much text on homepage 500 words is the estimate max.

```html
<!DOCTYPE html>
<html lang="en">
<head>
<meta charset="utf-8">
<title>Veltrix – ADSL2+ Unlimited &amp; Phone Line Rental</title>
<link rel="stylesheet" href="https://fonts.googleapis.com/css2?family=Oswald:wght@300;400;500;600&family=Questrial&family=Arimo:wght@400;700&display=swap">
<style>
  :root{
    --red:#f0372a;
    --red-dark:#c4231a;
    --black:#111111;
    --ink:#1a1a1a;
    --white:#ffffff;
    --grey-panel:#e6e6e6;
    --grey-footer:#e4e4e4;
    --field-border:#cfcfcf;
    --gold:#f6b52d;
    --card-top:#ffe34d;
    --card-bottom:#ff9a1c;
    --banner-text:#d9d9d9;
    --icon-grey:#dedede;
  }
  *{box-sizing:border-box;margin:0;padding:0}
  html,body{width:1145px;height:1200px;overflow:hidden;background:var(--white)}
  body{position:relative;font-family:"Arimo",Arial,sans-serif;color:var(--ink)}
  .abs{position:absolute}

  /* Header */
  .site-header{left:0;top:0;width:1145px;height:91px;background:var(--white);border-bottom:3px solid var(--red)}
  .brand{left:52px;top:23px;height:47px;display:flex;align-items:center;gap:12px}
  .brand-dot{width:46px;height:46px;border-radius:50%;background:var(--black)}
  .brand-name{font-family:"Questrial",sans-serif;font-size:34px;letter-spacing:2px;color:var(--black)}
  .action-btn{top:42px;height:33px;border-radius:8px;background:var(--red);color:var(--white);
    font-family:"Oswald",sans-serif;font-weight:500;font-size:21px;line-height:33px;text-align:center;letter-spacing:.3px}
  .btn-signup{left:506px;width:94px}
  .btn-check{left:606px;width:188px}
  .btn-chat{left:800px;width:106px}
  .call-label{left:938px;top:13px;font-family:"Oswald",sans-serif;font-size:15px;font-weight:300;color:var(--black);letter-spacing:-.2px}
  .call-number{left:938px;top:30px;font-family:"Oswald",sans-serif;font-size:37px;font-weight:500;color:var(--black);letter-spacing:-1px}

  /* Navigation */
  .main-nav{left:0;top:93px;width:1145px;height:50px;background:linear-gradient(#2a2a2a,#050505)}
  .nav-item{top:0;height:50px;line-height:50px;color:var(--white);font-family:"Questrial",sans-serif;font-size:18px}
  .nav-item.is-active{background:var(--red);text-align:center}

  /* Hero */
  .hero-photo{left:123px;top:143px;width:709px;height:362px;
    background:radial-gradient(ellipse at 40% 40%,#e9e3dd 0%,#cfcfd6 55%,#f4f4f6 100%)}
  .offer-banner{left:706px;top:143px;width:402px;height:333px}
  .offer-title{left:706px;top:166px;width:402px;text-align:center;font-family:"Oswald",sans-serif;font-weight:500;
    font-size:45px;line-height:51px;color:var(--banner-text)}
  .offer-price{left:706px;top:284px;width:402px;text-align:center;font-size:27px;color:var(--gold)}
  .btn-subscribe{left:801px;top:346px;width:222px;height:42px;border-radius:6px;border:2px solid var(--red-dark);
    background:linear-gradient(#ff5a47,var(--red-dark));color:var(--white);font-weight:700;font-size:16px;line-height:38px;text-align:center;letter-spacing:.5px}

  /* Content */
  .content-band{left:0;top:505px;width:1145px;height:527px;
    background:linear-gradient(#e3e5e8 0px,#ffffff 50px,#ffffff 440px,#e9e9e9 527px)}
  .section-title{font-family:"Questrial",sans-serif;font-size:35px;color:var(--black);letter-spacing:-.5px}
  .login-title{left:44px;top:552px}
  .login-box{left:37px;top:604px;width:519px;height:75px;border-radius:9px;background:var(--grey-panel)}
  .field{top:626px;height:32px;border:1px solid var(--field-border);border-radius:6px;background:var(--white);
    font-size:14px;color:#666;padding:0 12px;line-height:30px}
  .field-user{left:54px;width:176px}
  .field-pass{left:244px;width:175px}
  .btn-login{left:439px;top:627px;width:95px;height:30px;border-radius:4px;background:linear-gradient(#333,#000);
    color:var(--white);font-size:14px;line-height:30px;text-align:center}
  .about-title{left:45px;top:737px}
  .about-text{left:43px;top:799px;width:522px;font-size:14px;line-height:17px;color:var(--black)}
  .more-link{left:43px;top:916px;font-size:14px;color:var(--red)}

  .plans-title{left:651px;top:552px}
  .plan-card{top:614px;width:228px;height:300px;border-radius:9px;overflow:hidden;
    background:linear-gradient(160deg,var(--card-top) 0%,#ffc92e 45%,var(--card-bottom) 100%);
    box-shadow:-6px 4px 14px rgba(0,0,0,.25);text-align:center}
  .plan-metro{left:663px}
  .plan-regional{left:891px}
  .plan-ribbon{position:absolute;left:0;top:0}
  .plan-name{margin-top:18px;font-family:"Oswald",sans-serif;font-size:44px;font-weight:400;color:var(--black);line-height:52px}
  .plan-price{margin-top:4px;font-family:"Oswald",sans-serif;font-weight:300;font-size:40px;color:var(--white);line-height:46px}
  .plan-perk{margin-top:6px;font-weight:700;font-size:20px;line-height:22px;color:var(--white)}
  .plan-rate{margin-top:16px;font-family:"Oswald",sans-serif;font-weight:300;font-size:21px;color:var(--black);line-height:26px}
  .plan-divider{margin:10px auto 0;width:196px;height:1px;background:#c77a10}
  .plan-rate-small{margin-top:10px;font-family:"Oswald",sans-serif;font-weight:300;font-size:21px;line-height:22px;color:var(--black)}
  .plan-note{font-family:"Oswald",sans-serif;font-weight:300;font-size:15px;color:var(--black)}
  .plan-link{top:927px;display:flex;align-items:center;gap:10px;font-family:"Oswald",sans-serif;font-weight:300;font-size:17px;color:var(--red)}
  .plan-link-metro{left:666px}
  .plan-link-regional{left:897px}

  /* Footer */
  .footer-rule{left:0;top:1030px;width:1145px;height:2px;background:#d6d6d6}
  .social-bar{left:0;top:1047px;width:1145px;height:48px;background:var(--black)}
  .social-list{left:0;top:1055px;width:1145px;display:flex;justify-content:center;gap:11px}
  .social-icon{width:32px;height:32px;border-radius:50%;background:var(--icon-grey)}
  .site-footer{left:0;top:1095px;width:1145px;height:105px;background:var(--grey-footer)}
  .footer-nav{left:0;top:1116px;width:1145px;text-align:center;font-size:15px;color:var(--black)}
  .footer-nav span.sep{margin:0 8px}
  .copyright{left:0;top:1144px;width:1145px;text-align:center;font-size:13px;color:var(--red)}
</style>
</head>
<body>

<header class="abs site-header"></header>
<div class="abs brand"><span class="brand-dot"></span><span class="brand-name">VELTRIX</span></div>
<a class="abs action-btn btn-signup">SIGN UP</a>
<a class="abs action-btn btn-check">CHECK AVAILABLITY</a>
<a class="abs action-btn btn-chat">LIVE CHAT</a>
<div class="abs call-label">TO FIND OUT MORE OR JOIN CALL</div>
<div class="abs call-number">1300 55 18 90</div>

<nav class="abs main-nav">
  <a class="abs nav-item is-active" style="left:29px;width:101px">Home</a>
  <a class="abs nav-item" style="left:181px">About us</a>
  <a class="abs nav-item" style="left:328px">Products and Services</a>
  <a class="abs nav-item" style="left:581px">Pricing</a>
  <a class="abs nav-item" style="left:711px">Specials</a>
  <a class="abs nav-item" style="left:852px">Contact Us</a>
</nav>

<section>
  <div class="abs hero-photo" role="img" aria-label="Stock photo of a smiling businesswoman seated at a desk beside a computer monitor"></div>
  <svg class="abs offer-banner" width="402" height="333" viewBox="0 0 402 333" aria-hidden="true">
    <defs><linearGradient id="bannerFill" x1="0" y1="0" x2="0" y2="1"><stop offset="0" stop-color="#2c2c2c"/><stop offset="1" stop-color="#050505"/></linearGradient></defs>
    <polygon points="0,0 402,0 402,233 201,333 0,233" fill="url(#bannerFill)"/>
  </svg>
  <h1 class="abs offer-title">ADSL2+ Unlimited<br>&amp; Phone Line RentaL</h1>
  <div class="abs offer-price">for only $59.95</div>
  <a class="abs btn-subscribe">SUBSCRIBE PLAN</a>
</section>

<main>
  <div class="abs content-band"></div>

  <h2 class="abs section-title login-title">USER LOGIN</h2>
  <div class="abs login-box"></div>
  <div class="abs field field-user">username</div>
  <div class="abs field field-pass">password</div>
  <a class="abs btn-login">LOGIN</a>

  <h2 class="abs section-title about-title">ABOUT VELTRIX</h2>
  <p class="abs about-text">Veltrix's Duo2+ broadband and telephone plan is for Unlimited Broad band, line rental and for all calls which go over those lines. The plan requires the ADSL 2+ service, the telephone line and the pre-selection service (long distance and fixed to mobile calls) to be bundled. The service comes with a Wifi modem which is free but it will cost you $24.95 for delivery and handling and is a mandatory part of the service.</p>
  <a class="abs more-link">more info</a>

  <h2 class="abs section-title plans-title">DUO2+ PLANS</h2>

  <article class="abs plan-card plan-metro">
    <svg class="plan-ribbon" width="62" height="62" viewBox="0 0 62 62" aria-hidden="true">
      <polygon points="0,36 36,0 62,0 0,62" fill="var(--red)"/>
      <text x="20" y="38" transform="rotate(-45 20 38)" fill="#fff" font-family="Arimo,sans-serif" font-weight="700" font-size="9" text-anchor="middle">ON NET</text>
    </svg>
    <div class="plan-name">Metro</div>
    <div class="plan-price">$59.95</div>
    <div class="plan-perk">Free Set Up and<br>WIFI Modem</div>
    <div class="plan-rate">.18c per Local Calls</div>
    <div class="plan-divider"></div>
    <div class="plan-rate-small">.29c / minute</div>
    <div class="plan-note">Long Distance Calls</div>
  </article>

  <article class="abs plan-card plan-regional">
    <svg class="plan-ribbon" width="62" height="62" viewBox="0 0 62 62" aria-hidden="true">
      <polygon points="0,36 36,0 62,0 0,62" fill="var(--red)"/>
      <text x="20" y="38" transform="rotate(-45 20 38)" fill="#fff" font-family="Arimo,sans-serif" font-weight="700" font-size="9" text-anchor="middle">OFF NET</text>
    </svg>
    <div class="plan-name">Regional</div>
    <div class="plan-price">$79.95</div>
    <div class="plan-perk">Free Set Up and<br>WIFI Modem</div>
    <div class="plan-rate">.18c per Local Calls</div>
    <div class="plan-divider"></div>
    <div class="plan-rate-small">.29c / minute</div>
    <div class="plan-note">Long Distance Calls</div>
  </article>

  <a class="abs plan-link plan-link-metro">
    <svg width="20" height="20" viewBox="0 0 20 20" aria-hidden="true"><circle cx="10" cy="10" r="9" fill="#f7a21b"/><polygon points="8,6 14,10 8,14" fill="#fff"/></svg>
    SUBSCRIBE PLAN NOW</a>
  <a class="abs plan-link plan-link-regional">
    <svg width="20" height="20" viewBox="0 0 20 20" aria-hidden="true"><circle cx="10" cy="10" r="9" fill="#f7a21b"/><polygon points="8,6 14,10 8,14" fill="#fff"/></svg>
    SUBSCRIBE PLAN NOW</a>
</main>

<div class="abs footer-rule"></div>
<div class="abs social-bar"></div>
<div class="abs social-list">
  <a class="social-icon" aria-label="Chirpnet"></a>
  <a class="social-icon" aria-label="Chatterly"></a>
  <a class="social-icon" aria-label="Plexo +"></a>
  <a class="social-icon" aria-label="Linkwise"></a>
  <a class="social-icon" aria-label="News feed"></a>
</div>
<footer class="abs site-footer"></footer>
<nav class="abs footer-nav">ABOUT US<span class="sep">·</span>PRODUCTS AND SERVICES<span class="sep">·</span>PRICING<span class="sep">·</span>SPECIALS<span class="sep">·</span>CONTACT US</nav>
<div class="abs copyright">© Copyright 2013 Veltrix. All Rights Reserved</div>

</body>
</html>
```